Modern Website For Law Firm Lawyer Melbourne, Australia Coded

We are looking for a modern and sophisticated website design. We would prefer the site to be based on WordPress given it is intuitive and some of our staff have experience using it.

Our law firm is based in Melbourne, Australia and we deal with property. The website must be hosted on a reliable Australian server.

We would also appreciate it if the designer can provide some guidance about how to make changes/upload content, such as photos and articles. We are happy to pay for this advice.

We prefer classic fonts in black or grey. We would also like a dash of colour so please use a green, blue or aqua colour palette that is consistent with our logo attached.

We do not want any law related images - scales of justice, gavel or the like.

Our ultimate goal is to communicate that the firm is professional, affordable, modern, dynamic, knowledgeable and one with the community.

We would like the following pages/sections/icons:

1. Who We Are - we will provide content.

2. Our Services - 1. Property 2. Wills, 3. Powers of Attorney 4. Probate & Estate Administration 5.Consultancy & Agency- we will provide content for each of these sections.

3. Articles - we already have approximately 20 articles on a wordpress blog and would like to port these articles to the website. We can do this ourselves if the designer can give us instructions about how to do this. We would also like to give clients the option to subscribe to our articles.

4. Contact Us - this should include our firms contact details; location map and we would like to give clients the option to "Request A Quote" directly from the page - i.e they will need to provide their full name, phone number email address, choose subject from drop down menu and type a message that gets sent to our outlook email.

5. Terms and Conditions - we will provide content

We really like the style and photographs used in the following website and want something as close to this as possible:

https://www.brelwick.com/

For privacy reasons, we would prefer to provide content together with all business details once we have decided on the winner.

We will monitor entries closely and promise to provide feedback and guidance on each entry.

This project is guaranteed. If our budget is too low please email us so we can discuss further and perhaps increase our budget. We are reasonable in this regard.

Thank you very much for considering this project.

Target Market(s)

General public, professionals, lawyers and conveyancers

Industry/Entity Type

Law Firm

Coding

Coded - Design and coding required

Number of Pages Required

1 page

Font styles to use
Sans Serif

Colors
33b8a4
33a6d7
0692cd
3176b5
00a990
9bcb3c
86cfc6
cadf82
85acd3

Requirements
Must have
• 1. Site must be coded and hosted on a reliable Australian server and it would be much appreciated if the deisgner provides instructions about how to add photos, blog articles etc-
• 2. The site must be secure and have green lock at top of page
• 3. Request A Quote - name, email, phone, drop down subject, message - email to our outlook email
• 4. Article Subscription
• 5. Domain (we have already purchased)
• 6. Location map
• 7. Facebook, LinkedIn, Instagram Icons
• 8. Membership icons in this order - VLQ Member > Coastal Women Advocates > Guide For Counsel > Creature Foundation > Tovra > Parcelnet > Vek QA logos attached to go on bottom of page
• 9. Testimonials
Nice to have
• A modern, sophisticated website like:
• https://www.brelwick.com/ - we really like the style of the brelwick photographs
• We also really like this design by Rk of Sketch swarm:
• https://www.sketchswarm.com.au/design/58201946
Should not have
• Law related images - scales of justice gavel and the like

```html
<!DOCTYPE html>
<html lang="en">
<head>
<meta charset="utf-8">
<title>Ridgeline Lawyers</title>
<link href="https://fonts.googleapis.com/css2?family=Montserrat:wght@400;600;700&family=Open+Sans:wght@400;600;700&display=swap" rel="stylesheet">
<style>
:root{
  --teal:#2ab3c3;
  --blue:#1f6fb5;
  --blue-btn:#2d78c2;
  --ink:#222;
  --line:#cfd6da;
  --dark:#333333;
  --darker:#262626;
  --white:#fff;
}
*{box-sizing:border-box;margin:0;padding:0}
html,body{width:1200px;height:3243px;overflow:hidden}
body{position:relative;font-family:"Open Sans",Arial,sans-serif;color:var(--ink);background:var(--white)}
.abs{position:absolute}
h2.section-title{font-family:"Montserrat",Arial,sans-serif;font-weight:600;font-size:31px;text-align:center;letter-spacing:.5px}
.divider{position:absolute;left:50%;width:400px;margin-left:-200px;height:12px}
.divider::before{content:"";position:absolute;left:0;right:0;top:5px;height:1px;background:var(--line)}
.divider::after{content:"";position:absolute;left:194px;top:1px;width:10px;height:10px;border-radius:50%;border:2px solid var(--teal);background:var(--white)}
.on-color .divider::before{background:rgba(255,255,255,.45)}
.on-color .divider::after{background:transparent;border-color:rgba(255,255,255,.8)}

/* header */
.site-header{position:absolute;left:0;top:0;width:1200px;height:136px}
.brand{position:absolute;left:130px;top:22px;display:flex;align-items:center;gap:14px}
.brand-mark{width:60px;height:60px;border-radius:50%;background:var(--teal)}
.brand-name{font-family:"Montserrat",Arial,sans-serif;font-weight:400;font-size:22px;line-height:24px;color:#3a3a3a;letter-spacing:1px}
.header-call{position:absolute;left:610px;top:34px;display:flex;gap:12px;align-items:center}
.header-call p{font-family:"Montserrat",Arial,sans-serif;font-size:15px;color:#444;line-height:20px}
.header-call strong{display:block;font-size:20px;color:var(--blue-btn);font-weight:600}
.main-nav{position:absolute;left:119px;top:112px;width:962px;height:44px;background:var(--teal);display:flex;align-items:center;z-index:3}
.main-nav a{font-family:"Montserrat",Arial,sans-serif;font-weight:700;font-size:12px;color:#fff;text-decoration:none;text-transform:uppercase;margin-left:29px;margin-right:9px}
.nav-quote{position:absolute;right:0;top:0;height:44px;width:228px;background:var(--darker);color:#fff;font-family:"Montserrat",Arial,sans-serif;font-weight:700;font-size:15px;display:flex;align-items:center;justify-content:center;clip-path:polygon(16px 0,100% 0,100% 100%,0 100%)}

/* hero */
.hero{position:absolute;left:0;top:136px;width:1200px;height:526px}
.hero-photo{position:absolute;inset:0;background:
  radial-gradient(ellipse 160px 200px at 120px 260px,rgba(196,150,110,.85),transparent 70%),
  radial-gradient(ellipse 140px 210px at 280px 300px,rgba(70,70,80,.8),transparent 70%),
  radial-gradient(ellipse 170px 230px at 420px 240px,rgba(110,150,200,.85),transparent 70%),
  radial-gradient(ellipse 150px 190px at 560px 320px,rgba(120,110,105,.75),transparent 70%),
  radial-gradient(ellipse 170px 220px at 690px 280px,rgba(80,120,170,.8),transparent 70%),
  radial-gradient(ellipse 500px 120px at 400px 500px,rgba(240,240,240,.9),transparent 70%),
  linear-gradient(110deg,#b9ad9e 0%,#cfc5b6 30%,#dfe4e8 60%,#eef1f3 100%)}
.quote-form{position:absolute;left:735px;top:82px;width:340px;height:398px;background:rgba(255,255,255,.9);padding:20px 32px}
.quote-form h3{font-family:"Montserrat",Arial,sans-serif;font-weight:600;font-size:23px;text-align:center;margin-bottom:14px}
.field{height:30px;border:1px solid #c9c9c9;background:#fff;margin-bottom:9px;font-size:9px;color:#888;padding:9px 7px;text-transform:uppercase}
.field.msg{height:66px}
.agree{display:flex;align-items:center;gap:8px;font-size:12px;color:#444;margin:8px 0 10px}
.agree span{width:12px;height:12px;border:1px solid #999;background:#fff}
.btn-help{height:42px;background:var(--blue-btn);color:#fff;font-family:"Montserrat",Arial,sans-serif;font-weight:700;font-size:15px;display:flex;align-items:center;justify-content:center}

/* about */
.about{position:absolute;left:0;top:662px;width:1200px;height:343px}
.about h2{position:absolute;top:70px;width:100%}
.about .divider{top:118px}
.about-text{position:absolute;left:150px;width:900px;top:150px;text-align:center;font-size:12.5px;line-height:21px;color:#555}
.btn-outline{position:absolute;left:543px;top:244px;width:135px;height:37px;border:1px solid #333;font-size:12px;display:flex;align-items:center;justify-content:center;color:#222}

/* services */
.services{position:absolute;left:0;top:1005px;width:1200px;height:575px;background:
  radial-gradient(ellipse 220px 300px at 330px 250px,rgba(230,200,180,.35),transparent 70%),
  linear-gradient(115deg,#47bcb5 0%,#38aab8 40%,#1e74b8 80%,#1965ad 100%);color:#fff}
.services h2{position:absolute;top:40px;width:100%;color:#fff}
.services .divider{top:88px}
.service-label{position:absolute;font-family:"Montserrat",Arial,sans-serif;font-weight:700;font-size:16px;line-height:23px;color:#fff;text-transform:uppercase}

/* news */
.news{position:absolute;left:0;top:1580px;width:1200px;height:649px}
.news h2{position:absolute;top:68px;width:100%}
.news .divider{top:118px}
.news-card{position:absolute;top:204px;width:201px;height:335px;border:1px solid #e3e3e3;background:#fff}
.news-image{height:134px}
.news-card h4{font-family:"Open Sans",Arial,sans-serif;font-weight:700;font-size:12.5px;margin:18px 8px 4px;white-space:nowrap}
.news-meta{font-size:9px;color:#777;margin:0 8px 14px}
.news-card p{font-size:10.5px;line-height:15px;color:#666;margin:0 8px}
.read-more{position:absolute;right:48px;bottom:-1px;width:88px;height:22px;border:1px solid #ccc;font-size:9px;display:flex;align-items:center;justify-content:center;background:#fff}

/* map */
.map{position:absolute;left:0;top:2229px;width:1200px;height:214px;background:
  radial-gradient(ellipse 260px 110px at 250px 180px,rgba(120,180,230,.9),transparent 70%),
  radial-gradient(ellipse 500px 160px at 700px 120px,#f2efe8,transparent 75%),
  radial-gradient(ellipse 260px 80px at 1050px 60px,#eceae4,transparent 75%),
  linear-gradient(90deg,#6fb0e6 0%,#8cc0ea 22%,#e9e7e1 38%,#efece6 70%,#e4e6e8 100%)}
.map-btn{position:absolute;left:8px;top:8px;background:#fff;font-size:10px;padding:3px 7px;box-shadow:0 1px 2px rgba(0,0,0,.3)}

/* testimonials */
.testimonials{position:absolute;left:0;top:2443px;width:1200px;height:450px;background:linear-gradient(115deg,#3db7b5 0%,#2e98bf 50%,#1b68b0 100%);color:#fff}
.testimonials h2{position:absolute;top:40px;width:100%;color:#fff}
.testimonials .divider{top:90px}
.quote-card{position:absolute;top:182px;width:262px;height:108px;background:#fff;color:#333;font-size:11.5px;line-height:21px;padding:14px 30px}
.quote-card::after{content:"";position:absolute;left:26px;bottom:-10px;border-left:10px solid transparent;border-right:10px solid transparent;border-top:10px solid #fff}
.client{position:absolute;top:310px;display:flex;align-items:center;gap:22px}
.client-photo{width:54px;height:54px;border-radius:50%;border:3px solid #fff;background:radial-gradient(circle at 50% 40%,#d8b89c 0 30%,#5a4a42 60%,#e9e9e9 61%)}
.client-name{font-family:"Montserrat",Arial,sans-serif;font-size:10px;color:rgba(255,255,255,.35);letter-spacing:1px}
.dots{position:absolute;top:414px;left:584px;display:flex;gap:7px}
.dots i{width:7px;height:7px;border-radius:50%;background:rgba(255,255,255,.4)}
.dots i.on{background:#fff}

/* footer */
.site-footer{position:absolute;left:0;top:2893px;width:1200px;height:298px;background:var(--dark);color:#fff}
.footer-brand{position:absolute;left:134px;top:62px;display:flex;align-items:center;gap:14px}
.footer-brand .brand-name{color:#fff;font-size:24px;line-height:27px}
.search{position:absolute;left:130px;top:194px;width:270px;height:41px;display:flex}
.search span{flex:1;background:#fff;color:#999;font-size:11px;padding:13px 10px}
.search b{width:41px;background:#3aa3d4;display:flex;align-items:center;justify-content:center}
.footer-col h3{font-family:"Montserrat",Arial,sans-serif;font-weight:600;font-size:26px;margin-bottom:22px}
.contact-row{display:flex;gap:16px;font-size:11px;line-height:16px;margin-bottom:16px}
.contact-row .ic{width:18px;height:18px;border-radius:50%;background:#3aa3d4;flex:none;display:flex;align-items:center;justify-content:center}
.recent p{font-family:"Montserrat",Arial,sans-serif;font-size:10.5px;font-weight:600;line-height:15px;margin-bottom:14px;text-transform:uppercase}
.social{display:flex;gap:10px;margin-top:8px}
.social i{width:28px;height:28px;border-radius:50%;background:#6a6a6a;display:block}
.footer-bar{position:absolute;left:0;top:3191px;width:1200px;height:52px;background:var(--darker);color:#bbb;font-size:11.5px;display:flex;align-items:center;justify-content:center}
</style>
</head>
<body>

<header class="site-header">
  <div class="brand"><span class="brand-mark"></span><span class="brand-name">RIDGELINE<br>LAWYERS</span></div>
  <div class="header-call">
    <svg width="30" height="30" viewBox="0 0 30 30"><circle cx="15" cy="15" r="13" fill="none" stroke="#444" stroke-width="2"/><path d="M10 8l3 0 1 4-2 1.5c1 2 2.5 3.5 4.5 4.5l1.5-2 4 1v3c-6 0.5-12-5.5-12-12z" fill="#444"/></svg>
    <p>Call Us to Get Started Today<strong>(555) 340-2210</strong></p>
  </div>
  <nav class="main-nav">
    <a>Home</a><a>About H&amp;P</a><a>Attorneys</a><a>Practice Areas</a><a>Results</a><a>News</a><a>Contact Us</a>
    <span class="nav-quote">REQUEST A QUOTE</span>
  </nav>
</header>

<section class="hero">
  <div class="hero-photo" role="img" aria-label="Photograph of a team of lawyers working together around a laptop"></div>
  <form class="quote-form">
    <h3>REQUEST A QUOTE</h3>
    <div class="field">Name</div>
    <div class="field">Phone Number</div>
    <div class="field">Email Address</div>
    <div class="field">Subject</div>
    <div class="field msg">How can we help?</div>
    <div class="agree"><span></span>I have read the Disclaimer</div>
    <div class="btn-help">GET HELP NOW</div>
  </form>
</section>

<section class="about">
  <h2 class="section-title">ABOUT RIDGELINE LAWYERS</h2>
  <div class="divider"></div>
  <p class="about-text">The cases we represent span the spectrum, from catastrophic physical injuries to complex business disputes. Our trial lawyers bring our talents and expertise to redress wrongs, seek justice and protect the futures of our clients. With more than 20 trial lawyers in the firm, Harrow &amp; Pell welcomes every opportunity to try a case when it is right for our clients. In fact, we prepare every case for it.</p>
  <div class="btn-outline">Read more +</div>
</section>

<section class="services on-color" role="img" aria-label="Services section over a teal-tinted photograph of a smiling client">
  <h2 class="section-title">OUR SERVICES</h2>
  <div class="divider"></div>
  <svg class="abs" style="left:0;top:0" width="1200" height="575" viewBox="0 0 1200 575">
    <path d="M325 494 A270 270 0 0 1 853 494" fill="none" stroke="#dfe4e8" stroke-width="10"/>
    <g fill="none" stroke="#fff" stroke-width="1.5">
      <polyline points="172,266 330,266 380,318"/>
      <polyline points="152,412 270,412 300,462"/>
      <line x1="589" y1="212" x2="589" y2="226"/>
      <polyline points="1000,284 850,284 815,318"/>
      <polyline points="1060,414 930,414 880,462"/>
    </g>
    <g>
      <circle cx="589" cy="280" r="66" fill="#1f3d4f"/><circle cx="589" cy="280" r="56" fill="#fff"/>
      <circle cx="398" cy="359" r="66" fill="#1f3d4f"/><circle cx="398" cy="359" r="56" fill="#fff"/>
      <circle cx="780" cy="359" r="66" fill="#1f3d4f"/><circle cx="780" cy="359" r="56" fill="#fff"/>
      <circle cx="330" cy="500" r="66" fill="#1f3d4f"/><circle cx="330" cy="500" r="56" fill="#fff"/>
      <circle cx="848" cy="500" r="66" fill="#1f3d4f"/><circle cx="848" cy="500" r="56" fill="#fff"/>
    </g>
    <g fill="#2d3b45">
      <rect x="573" y="274" width="32" height="14" rx="2"/><circle cx="580" cy="267" r="4"/><circle cx="598" cy="267" r="4"/>
      <circle cx="398" cy="349" r="8"/><path d="M384 372q14-16 28 0z"/>
      <circle cx="772" cy="352" r="5"/><circle cx="789" cy="352" r="5"/><path d="M764 372q8-12 16 0zM781 372q8-12 16 0z"/>
      <path d="M315 488h30v20h-18l-7 6v-6h-5z" fill="none" stroke="#2d3b45" stroke-width="2.5"/>
      <circle cx="848" cy="490" r="8"/><path d="M834 514q14-18 28 0z"/>
    </g>
  </svg>
  <span class="service-label" style="left:504px;top:178px">Powers of Attorney</span>
  <span class="service-label" style="left:192px;top:236px">Property</span>
  <span class="service-label" style="left:870px;top:226px">Probate &amp; Estate<br>Administration</span>
  <span class="service-label" style="left:160px;top:382px">Wills</span>
  <span class="service-label" style="left:927px;top:360px">Consultancy &amp;<br>Agency</span>
</section>

<section class="news">
  <h2 class="section-title">LATEST NEWS</h2>
  <div class="divider"></div>
  <article class="news-card" style="left:132px">
    <div class="news-image" role="img" aria-label="Photograph of hands using a calculator" style="background:radial-gradient(ellipse 70px 50px at 70px 70px,#e6a98a,transparent 75%),linear-gradient(135deg,#e9eef2,#9fb3c4 70%,#5f6f7d)"></div>
    <h4>Developing a marketing plan</h4><p class="news-meta">by Mr Adler on at January 14, 2016</p>
    <p>Lorem ipsum dolor sit amet, consectetur adipiscing elit. Integer nec odio. Praesent libero. Sed cursus ante dapibus diam. Sed nisi. Nulla quis sem at nibh elementum imperdiet. Duis sagittis ipsum....</p>
    <span class="read-more">READ MORE</span>
  </article>
  <article class="news-card" style="left:376px">
    <div class="news-image" role="img" aria-label="Photograph of hands reviewing charts on paper" style="background:radial-gradient(ellipse 80px 45px at 110px 60px,#d8a88c,transparent 75%),linear-gradient(135deg,#ffffff,#cfdbe6 55%,#3f78b5)"></div>
    <h4>Developing a marketing plan</h4><p class="news-meta">by Mr Adler on at January 14, 2016</p>
    <p>Lorem ipsum dolor sit amet, consectetur adipiscing elit. Integer nec odio. Praesent libero. Sed cursus ante dapibus diam. Sed nisi. Nulla quis sem at nibh elementum imperdiet. Duis sagittis ipsum....</p>
    <span class="read-more">READ MORE</span>
  </article>
  <article class="news-card" style="left:620px">
    <div class="news-image" role="img" aria-label="Photograph of an office team at computers" style="background:radial-gradient(ellipse 90px 40px at 100px 110px,#6a8fb8,transparent 75%),linear-gradient(180deg,#c9ccd0 0%,#5c6672 45%,#2e343c)"></div>
    <h4>Developing a marketing plan</h4><p class="news-meta">by Mr Adler on at January 14, 2016</p>
    <p>Lorem ipsum dolor sit amet, consectetur adipiscing elit. Integer nec odio. Praesent libero. Sed cursus ante dapibus diam. Sed nisi. Nulla quis sem at nibh elementum imperdiet. Duis sagittis ipsum....</p>
    <span class="read-more">READ MORE</span>
  </article>
  <article class="news-card" style="left:866px">
    <div class="news-image" role="img" aria-label="Photograph of hands typing on a keyboard" style="background:radial-gradient(ellipse 70px 50px at 70px 50px,#c89a82,transparent 75%),linear-gradient(135deg,#8a8684,#3a3a3d 60%,#1f1f22)"></div>
    <h4>Developing a marketing plan</h4><p class="news-meta">by Mr Adler on at January 14, 2016</p>
    <p>Lorem ipsum dolor sit amet, consectetur adipiscing elit. Integer nec odio. Praesent libero. Sed cursus ante dapibus diam. Sed nisi. Nulla quis sem at nibh elementum imperdiet. Duis sagittis ipsum....</p>
    <span class="read-more">READ MORE</span>
  </article>
</section>

<section class="map" role="img" aria-label="Location map of Europe with office markers">
  <span class="map-btn">Map</span>
  <svg class="abs" style="left:395px;top:48px" width="70" height="70" viewBox="0 0 70 70">
    <circle cx="34" cy="34" r="34" fill="#2bb3a6"/><path d="M34 22a9 9 0 0 1 9 9c0 7-9 16-9 16s-9-9-9-16a9 9 0 0 1 9-9z" fill="#1d3b44"/><circle cx="34" cy="31" r="3.5" fill="#2bb3a6"/>
  </svg>
  <svg class="abs" style="left:538px;top:34px" width="70" height="70" viewBox="0 0 70 70">
    <circle cx="35" cy="35" r="34" fill="#2bb3a6"/><path d="M35 23a9 9 0 0 1 9 9c0 7-9 16-9 16s-9-9-9-16a9 9 0 0 1 9-9z" fill="#1d3b44"/><circle cx="35" cy="32" r="3.5" fill="#2bb3a6"/>
  </svg>
</section>

<section class="testimonials on-color">
  <h2 class="section-title">CLIENT TESTIMONIALS</h2>
  <div class="divider"></div>
  <blockquote class="quote-card" style="left:147px">" But I must explain to you the how all this mistaken idea of thealorem qco denouncing pleasure"</blockquote>
  <blockquote class="quote-card" style="left:473px">" But I must explain to you the how all this mistaken idea of thealorem qco denouncing pleasure"</blockquote>
  <blockquote class="quote-card" style="left:802px">" But I must explain to you the how all this mistaken idea of thealorem qco denouncing pleasure"</blockquote>
  <div class="client" style="left:146px"><span class="client-photo" role="img" aria-label="Client portrait"></span><span class="client-name">MARK PINE</span></div>
  <div class="client" style="left:473px"><span class="client-photo" role="img" aria-label="Client portrait"></span><span class="client-name">MARK PINE</span></div>
  <div class="client" style="left:800px"><span class="client-photo" role="img" aria-label="Client portrait"></span><span class="client-name">MARK PINE</span></div>
  <div class="dots"><i></i><i></i><i class="on"></i></div>
</section>

<footer class="site-footer">
  <div class="footer-brand"><span class="brand-mark"></span><span class="brand-name">RIDGELINE<br>LAWYERS</span></div>
  <div class="search"><span>Search this Site</span><b><svg width="18" height="18" viewBox="0 0 18 18"><circle cx="7.5" cy="7.5" r="5.5" fill="none" stroke="#fff" stroke-width="2"/><line x1="11.5" y1="11.5" x2="16" y2="16" stroke="#fff" stroke-width="2"/></svg></b></div>
  <div class="footer-col abs" style="left:528px;top:54px;width:230px">
    <h3>Get in Touch</h3>
    <div class="contact-row"><span class="ic"><svg width="10" height="12" viewBox="0 0 10 12"><path d="M5 0a4 4 0 0 1 4 4c0 3-4 8-4 8S1 7 1 4a4 4 0 0 1 4-4z" fill="#fff"/></svg></span><p><b>RIDGELINE LAWYERS</b><br>1180 Larkfield Avenue<br>Suite 300<br>Riverton, MO 60412</p></div>
    <div class="contact-row"><span class="ic"><svg width="10" height="10" viewBox="0 0 10 10"><path d="M1 1h3l1 2.5-1.5 1c.8 1.5 1.5 2.2 3 3l1-1.5L10 7v2.5C5 10 0 5 1 1z" fill="#fff"/></svg></span><p>(555) 340-2210</p></div>
    <div class="contact-row"><span class="ic"><svg width="10" height="10" viewBox="0 0 10 10"><rect x="1" y="3" width="8" height="6" fill="#fff"/><rect x="3" y="0.5" width="4" height="3" fill="#fff"/></svg></span><p>(555) 340-2277</p></div>
  </div>
  <div class="footer-col recent abs" style="left:798px;top:54px;width:300px">
    <h3>RECENT NEWS</h3>
    <p>Wrongful death award – $6.7 million</p>
    <p>Westmere federal court denies motion to dismiss Calmora suit</p>
    <p>Client wins $5.7 million in Mesh-Alvero verdict against Brandt &amp; Colley</p>
    <div class="social"><i></i><i></i><i></i><i></i><i></i></div>
  </div>
</footer>
<div class="footer-bar">Copyright © 2017 Harrow &amp; Pell, LLP. | All Rights Reserved |Disclaimer</div>

</body>
</html>
```